need 4 creative A frame (SANDWICH BOARD) designs concepts for dental office

need 4 creative A frame (SANDWICH BOARD) designs concepts
1 - targeting kids
2. targeting old age
3. targeting teens
4 targeting general public

website - www.brenvaxdental.ca

LINK for Measurements for sandwich board https://www.korvepa.ca/BL_1921/Aluminum-Snap-Edge-A-Frame-Sign

i am attaching certain key ingredients ( rough sketch in uploaded files ) to be added on each design though not mandatory if the design is very creative

```html
<!DOCTYPE html>
<html lang="en">
<head>
<meta charset="utf-8">
<title>Brenvax Dental – A-Frame Board</title>
<link rel="stylesheet" href="https://fonts.googleapis.com/css2?family=Oswald:wght@200;300;400;600&family=Arimo:wght@400;700&display=swap">
<style>
  :root {
    --slate: #6b6e72;
    --white: #ffffff;
    --sky: #45c0e8;
    --sky-deep: #1c8ec4;
    --badge-text: #1679a8;
    --bar-light: #e6e7e8;
    --ink: #0d0d0d;
  }
  html, body {
    margin: 0;
    padding: 0;
    width: 943px;
    height: 1200px;
    overflow: hidden;
    background: var(--white);
  }
  .board {
    position: relative;
    width: 1200px;
    height: 1526px;
    transform: scale(0.78583);
    transform-origin: 0 0;
    overflow: hidden;
    background: var(--white);
    font-family: "Oswald", sans-serif;
  }
  .backdrop {
    position: absolute;
    inset: 0;
  }
  .badge {
    position: absolute;
    left: 55px;
    top: 635px;
    width: 320px;
    height: 320px;
  }
  .badge-label {
    position: absolute;
    left: 0;
    right: 0;
    top: 70px;
    text-align: center;
    font-family: "Arimo", sans-serif;
    font-weight: 700;
    font-size: 36px;
    color: var(--badge-text);
    letter-spacing: 0.5px;
  }
  .slogan {
    position: absolute;
    color: var(--white);
    text-transform: uppercase;
    line-height: 1;
    white-space: nowrap;
  }
  .slogan .strong { font-weight: 600; }
  .slogan .soft { font-weight: 300; }
  .slogan-top {
    left: 428px;
    top: 752px;
    font-size: 78px;
  }
  .slogan-top .soft { font-size: 56px; }
  .price-bar {
    position: absolute;
    left: 340px;
    top: 850px;
    width: 490px;
    height: 96px;
    background: linear-gradient(180deg, #f4f4f5 0%, var(--bar-light) 100%);
    box-shadow: 0 3px 6px rgba(0,0,0,0.25);
    display: flex;
    align-items: center;
    justify-content: flex-end;
    padding-right: 30px;
    box-sizing: border-box;
  }
  .price-bar span {
    font-weight: 200;
    font-size: 80px;
    color: var(--sky-deep);
    text-transform: uppercase;
    line-height: 1;
  }
  .slogan-bottom {
    left: 862px;
    top: 858px;
    font-size: 78px;
  }
  .slogan-bottom .soft { font-size: 56px; }
  .brand {
    position: absolute;
    left: 0;
    right: 0;
    top: 1075px;
    display: flex;
    justify-content: center;
    align-items: center;
    gap: 22px;
  }
  .brand-dot {
    width: 34px;
    height: 34px;
    border-radius: 50%;
    background: var(--sky);
  }
  .brand-name {
    font-family: "Oswald", sans-serif;
    font-weight: 400;
    font-size: 118px;
    color: var(--sky);
    line-height: 1;
    letter-spacing: 1px;
  }
  .intake {
    position: absolute;
    left: 365px;
    top: 1344px;
    width: 471px;
    height: 52px;
    border-radius: 26px;
    background: var(--ink);
    color: var(--white);
    font-family: "Arimo", sans-serif;
    font-size: 31px;
    display: flex;
    align-items: center;
    justify-content: center;
  }
  .phone {
    position: absolute;
    left: 0;
    right: 0;
    top: 1424px;
    text-align: center;
    font-family: "Arimo", sans-serif;
    font-weight: 700;
    font-size: 78px;
    color: var(--sky);
    line-height: 1;
    letter-spacing: 1px;
  }
</style>
</head>
<body>
  <main class="board">
    <svg class="backdrop" width="1200" height="1526" viewBox="0 0 1200 1526">
      <defs>
        <linearGradient id="photoTone" x1="0" y1="0" x2="0.3" y2="1">
          <stop offset="0" stop-color="#8c8e92"/>
          <stop offset="0.45" stop-color="#5d5a5c"/>
          <stop offset="1" stop-color="#e2b7c4"/>
        </linearGradient>
      </defs>
      <rect class="slate-field" x="0" y="0" width="1200" height="1526" fill="var(--slate)"/>
      <path class="white-sweep" d="M0,555 Q380,1010 1200,1030 L1200,1526 L0,1526 Z" fill="var(--white)"/>
      <circle class="photo-window" cx="760" cy="160" r="570" fill="url(#photoTone)" role="img" aria-label="Photo: a surprised young girl in a dental chair covering her mouth, with a dentist's gloved hands holding instruments on either side"/>
    </svg>

    <div class="badge">
      <svg width="320" height="320" viewBox="0 0 320 320">
        <circle cx="160" cy="160" r="160" fill="var(--white)"/>
        <circle cx="160" cy="160" r="150" fill="var(--sky)"/>
        <g fill="none" stroke="var(--white)" stroke-width="30" stroke-linejoin="miter">
          <polyline points="95,140 45,190 95,240"/>
          <polyline points="175,140 125,190 175,240"/>
          <polyline points="255,140 205,190 255,240"/>
        </g>
      </svg>
      <div class="badge-label">WE’RE IN</div>
    </div>

    <div class="slogan slogan-top"><span class="strong">Dentistry</span> <span class="soft">is not</span></div>
    <div class="price-bar"><span>Expensive</span></div>
    <div class="slogan slogan-bottom"><span class="strong">Neglect</span> <span class="soft">is !</span></div>

    <div class="brand">
      <span class="brand-dot"></span>
      <span class="brand-name">Brenvax Dental</span>
    </div>

    <div class="intake">Accepting New Patients</div>
    <div class="phone">587 555 0148</div>
  </main>
</body>
</html>
```